Business cards for a recruitment company
Marrowby Associates
Modern
Helena Marrowby
Managing Director
PO Box 48213 Corvel Harbour Plaza Dubai United Arab Emirates
lena@marrowbyassociates-mail.test
marrowbyassociates-mail.test
The business card needs to have my name, designation etc in both English and Arabic. Therefore, both languages will appear on the front of the card. The final design will illustrate how two different translations will appear on the front of the card. **The logo must also appear on the front of the card.
The back of the card will be plain white with just the logo as attached in the AI file. Perhaps the logo could be indented.

```html
<!DOCTYPE html>
<html lang="en">
<head>
<meta charset="utf-8">
<title>Marrowby Associates – Business Cards</title>
<link rel="stylesheet" href="https://fonts.googleapis.com/css2?family=Cinzel:wght@500&family=Open+Sans:wght@400;600&family=Noto+Naskh+Arabic:wght@500&display=swap">
<style>
  :root {
    --stage: #2a2a2c;
    --ink: #111112;
    --paper: #ffffff;
    --violet: #8a5ea8;
    --violet-soft: #b895cf;
    --grey-text: #4a4a4e;
    --light-text: #e4e4e7;
  }
  * { box-sizing: border-box; margin: 0; padding: 0; }
  html, body { width: 1200px; height: 698px; overflow: hidden; }
  body {
    background: var(--stage);
    font-family: "Open Sans", Arial, sans-serif;
    position: relative;
  }
  .card {
    position: absolute;
    width: 520px;
    height: 300px;
    border-radius: 16px;
    overflow: hidden;
    box-shadow: 0 14px 30px rgba(0,0,0,.45);
  }
  .card--back { left: 50px; top: 120px; background: var(--ink); }
  .card--front { left: 630px; top: 278px; background: var(--paper); }

  .wordmark { display: flex; align-items: center; gap: 14px; }
  .wordmark__dot { width: 34px; height: 34px; border-radius: 50%; background: var(--violet); flex: none; }
  .wordmark__name {
    font-family: "Cinzel", Georgia, serif;
    font-weight: 500;
    line-height: 1.05;
    letter-spacing: .06em;
  }
  .wordmark__name span { display: block; }
  .wordmark__name .second { letter-spacing: .38em; font-size: .62em; }

  .card--back .wordmark { position: absolute; left: 110px; top: 112px; }
  .card--back .wordmark__name { color: var(--paper); font-size: 34px; }
  .card--back .website {
    position: absolute; left: 0; right: 0; bottom: 58px;
    text-align: center; color: var(--light-text);
    font-size: 12px; letter-spacing: .28em;
  }

  .card--front .swoosh { position: absolute; inset: 0; width: 100%; height: 100%; }
  .card--front .wordmark { position: absolute; left: 40px; top: 60px; }
  .card--front .wordmark__dot { width: 26px; height: 26px; }
  .card--front .wordmark__name { color: var(--ink); font-size: 26px; }

  .person { position: absolute; left: 40px; top: 150px; }
  .person__name { color: var(--violet); font-size: 13px; font-weight: 600; letter-spacing: .12em; text-transform: uppercase; }
  .person__role { color: var(--grey-text); font-size: 9px; letter-spacing: .16em; text-transform: uppercase; margin-top: 2px; }
  .person__name-ar, .person__role-ar {
    font-family: "Noto Naskh Arabic", "Times New Roman", serif;
    direction: rtl; text-align: left; unicode-bidi: plaintext;
  }
  .person__name-ar { color: var(--violet); font-size: 15px; margin-top: 6px; }
  .person__role-ar { color: var(--grey-text); font-size: 11px; }

  .address {
    position: absolute; left: 40px; bottom: 26px;
    color: var(--grey-text); font-size: 9.5px; line-height: 1.45;
  }

  .contacts {
    position: absolute; right: 14px; top: 142px;
    list-style: none; color: var(--light-text);
    font-size: 8px; line-height: 1;
  }
  .contacts li { display: flex; align-items: center; justify-content: flex-end; gap: 5px; margin-bottom: 8px; white-space: nowrap; }
  .contacts svg { width: 10px; height: 10px; flex: none; }
</style>
</head>
<body>

  <section class="card card--back" aria-label="Card back">
    <div class="wordmark">
      <span class="wordmark__dot"></span>
      <p class="wordmark__name"><span>Marrowby</span><span class="second">Associates</span></p>
    </div>
    <p class="website">www.marrowbyassociates-mail.test</p>
  </section>

  <section class="card card--front" aria-label="Card front">
    <svg class="swoosh" viewBox="0 0 520 300" preserveAspectRatio="none" aria-hidden="true">
      <path d="M270 0 H520 V300 H300 C335 200 335 80 270 0 Z" fill="var(--ink)"/>
      <path d="M252 0 C345 85 340 200 284 300" fill="none" stroke="var(--violet)" stroke-width="6"/>
      <path d="M238 0 C328 80 322 200 266 300" fill="none" stroke="var(--violet-soft)" stroke-width="1.5"/>
    </svg>

    <div class="wordmark">
      <span class="wordmark__dot"></span>
      <p class="wordmark__name"><span>Marrowby</span><span class="second">Associates</span></p>
    </div>

    <div class="person">
      <p class="person__name">Helena Marrowby</p>
      <p class="person__role">Managing Director</p>
      <p class="person__name-ar" lang="ar">هيلينا ماروبي</p>
      <p class="person__role-ar" lang="ar">المدير العام</p>
    </div>

    <p class="address">PO Box 48213 Corvel Harbour Plaza<br>Dubai, United Arab Emirates</p>

    <ul class="contacts">
      <li>+971 4 555 0142
        <svg viewBox="0 0 12 12"><path d="M3 1 L5 3.5 L4 5 C4.6 6.4 5.6 7.4 7 8 L8.5 7 L11 9 L9.8 11 C5 10.6 1.4 7 1 2.2 Z" fill="currentColor"/></svg></li>
      <li>+971 4 555 0187
        <svg viewBox="0 0 12 12"><rect x="1" y="3" width="10" height="7" rx="1" fill="none" stroke="currentColor"/><rect x="3" y="1" width="6" height="3" fill="currentColor"/></svg></li>
      <li>+971 50 555 0163
        <svg viewBox="0 0 12 12"><rect x="3.2" y="1" width="5.6" height="10" rx="1" fill="none" stroke="currentColor"/><circle cx="6" cy="9.3" r=".7" fill="currentColor"/></svg></li>
      <li>lena@marrowbyassociates-mail.test
        <svg viewBox="0 0 12 12"><rect x="1" y="2.5" width="10" height="7" fill="none" stroke="currentColor"/><path d="M1 2.5 L6 6.5 L11 2.5" fill="none" stroke="currentColor"/></svg></li>
      <li>marrowbyassociates-mail.test
        <svg viewBox="0 0 12 12"><circle cx="6" cy="6" r="4.8" fill="none" stroke="currentColor"/><path d="M1.2 6 H10.8 M6 1.2 C3.6 4 3.6 8 6 10.8 M6 1.2 C8.4 4 8.4 8 6 10.8" fill="none" stroke="currentColor" stroke-width=".8"/></svg></li>
    </ul>
  </section>

</body>
</html>
```